Social Media Graphics - ALL TEXT RK

We are looking for a series of social media graphics for Instagram (standard size 1:1 (1080x1080px) that are ALL TEXT. We want the following quotes below on each graphic; one quote per graphic. AND, In very small letters at the bottom of each graphic, add @RKMarlowLive

The look and feel of these graphics should be complimentary to the color palette attached below; but keep them simple. But the design is up to you; at the end of this document, I provided various samples of all text graphics that I like as examples.

Target Market(s)

women looking to lose weight

Industry/Entity Type

health and wellness

Colors
E54698
E96AAD
F1A4CE
F9D9EA
FCEFF6

Requirements
Must have
• the quotes in the document
Should not have
• no stock photography

```html
<!DOCTYPE html>
<html lang="en">
<head>
<meta charset="utf-8">
<title>RK Social Graphics – All Text Series</title>
<link rel="stylesheet" href="https://fonts.googleapis.com/css2?family=Bebas+Neue&family=Oswald:wght@500;600&family=Open+Sans:wght@400;600;700&family=Poppins:wght@700;800&family=Sniglet:wght@800&display=swap">
<style>
  :root {
    --white: #ffffff;
    --black: #000000;
    --magenta: #d4145a;
    --deep-rose: #cf0065;
    --hot-pink: #fe0787;
    --bright-pink: #f0449a;
    --candy: #fb6aaf;
    --bubblegum: #f99bcc;
    --blush: #fcd1e6;
    --petal: #f9d9ea;
    --paper: #efc4d8;
    --raspberry: #d4006a;
  }
  * { box-sizing: border-box; margin: 0; padding: 0; }
  html, body { width: 1200px; height: 896px; overflow: hidden; background: var(--white); }
  .board { position: relative; width: 1200px; height: 896px; }

  .post { position: absolute; width: 271px; height: 271px; overflow: hidden; }
  .post--outlined { border: 1px solid var(--bright-pink); background: var(--white); }
  .handle {
    position: absolute; left: 0; right: 0; text-align: center;
    font: 700 6.5px/1 "Open Sans", sans-serif; color: var(--magenta);
  }

  /* 1 – GLP-1 secret */
  .post-glp { left: 20px; top: 17px; }
  .post-glp .intro { position: absolute; left: 46px; top: 56px; font: 400 16px/15px "Open Sans", sans-serif; color: var(--magenta); }
  .post-glp .claim { position: absolute; left: 46px; top: 116px; font: 500 20px/25px "Oswald", sans-serif; color: var(--bright-pink); text-transform: uppercase; }
  .post-glp .highlight { background: var(--bright-pink); color: var(--white); padding: 0 4px; margin-left: -4px; }
  .post-glp .handle { top: 247px; }

  /* 2 – natural boost */
  .post-boost { left: 306px; top: 17px; background: var(--candy); }
  .post-boost .headline {
    position: absolute; left: 36px; top: 26px; right: 30px;
    font: 400 30px/25px "Bebas Neue", sans-serif; color: var(--petal);
    text-shadow: 2px 2px 0 var(--magenta);
  }
  .post-boost .headline span { display: block; margin-top: 24px; }
  .post-boost .handle { top: 247px; }

  /* 3 – lied to */
  .post-lied { left: 590px; top: 17px; }
  .post-lied .title { position: absolute; left: 0; right: 0; top: 92px; text-align: center; font: 400 33px/1 "Bebas Neue", sans-serif; color: var(--black); }
  .post-lied .sub { position: absolute; left: 0; right: 0; top: 151px; text-align: center; font: 400 17px/15px "Bebas Neue", sans-serif; color: var(--magenta); }
  .post-lied .handle { top: 203px; }

  /* 4 – stubborn belly fat */
  .post-fault { left: 873px; top: 17px; background: var(--blush); }
  .post-fault .title { position: absolute; left: 0; right: 0; top: 74px; text-align: center; font: 600 33px/29px "Oswald", sans-serif; color: var(--magenta); text-transform: uppercase; transform: scaleX(0.9); }
  .post-fault .sub { position: absolute; left: 0; right: 0; top: 196px; text-align: center; font: 400 17px/1 "Bebas Neue", sans-serif; color: var(--magenta); }
  .post-fault .handle { top: 249px; }

  /* 5 – frustrated */
  .post-frustrated { left: 22px; top: 304px; background: var(--deep-rose); color: var(--white); text-align: center; }
  .post-frustrated .title { position: absolute; left: 0; right: 0; top: 66px; font: 400 19px/23px "Open Sans", sans-serif; }
  .post-frustrated .body { position: absolute; left: 30px; right: 30px; top: 136px; font: 400 12.5px/22.6px "Open Sans", sans-serif; }
  .post-frustrated .handle { top: 249px; color: var(--white); }

  /* 6 – hormones */
  .post-hormones { left: 306px; top: 304px; background: var(--hot-pink); }
  .post-hormones .title { position: absolute; left: 31px; top: 46px; font: 400 35px/27.5px "Bebas Neue", sans-serif; color: var(--black); }
  .post-hormones .sub { position: absolute; left: 31px; top: 166px; font: 400 19px/19px "Open Sans", sans-serif; color: var(--black); }
  .post-hormones .handle { top: 249px; color: var(--black); }

  /* 7 – finally */
  .post-finally { left: 587px; top: 304px; background: var(--bubblegum); }
  .post-finally .word { position: absolute; left: 49px; top: 56px; font: 400 54px/1 "Bebas Neue", sans-serif; color: var(--raspberry); }
  .post-finally .sub { position: absolute; left: 49px; top: 108px; font: 400 24px/22.6px "Bebas Neue", sans-serif; color: var(--white); }
  .post-finally .handle { top: 249px; }

  /* 8 – one supplement */
  .post-overnight { left: 868px; top: 304px; background: var(--paper); }
  .post-overnight .strokes { position: absolute; inset: 0; }
  .post-overnight .message {
    position: absolute; left: 10px; right: 0; top: 60px; text-align: center;
    font: 800 19px/20px "Sniglet", sans-serif; color: var(--magenta); letter-spacing: 1.5px;
    text-transform: uppercase; transform: rotate(-20deg);
  }
  .post-overnight .message span { display: block; margin-top: 26px; }
  .post-overnight .handle { top: 255px; left: 190px; right: auto; }

  /* 9 – bloating */
  .post-bloating { left: 303px; top: 592px; background: var(--black); }
  .post-bloating .title { position: absolute; left: 55px; top: 70px; font: 700 18.5px/18px "Poppins", sans-serif; color: var(--petal); }
  .post-bloating .sub { position: absolute; left: 55px; top: 144px; font: 700 12.5px/15px "Poppins", sans-serif; color: var(--hot-pink); }
  .post-bloating .handle { top: 255px; left: 210px; right: auto; color: var(--hot-pink); }

  /* 10 – wake up */
  .post-wake { left: 587px; top: 592px; background: linear-gradient(210deg, #fbd0e6 0%, #fb5fae 35%, var(--hot-pink) 65%, var(--raspberry) 100%); }
  .post-wake .title { position: absolute; left: 19px; top: 74px; font: 800 17.5px/18.4px "Poppins", sans-serif; color: var(--white); text-transform: uppercase; }
  .post-wake .handle { top: 255px; left: 210px; right: auto; color: var(--white); }
</style>
</head>
<body>
<main class="board">

  <section class="post post--outlined post-glp">
    <p class="intro">GLP-1: the magic behind<br>the weight loss drugs.</p>
    <p class="claim">But here's the secret -<br>you can boost it<br><span class="highlight">naturally</span> without<br>a prescription!</p>
    <p class="handle">@RKMarlowLive</p>
  </section>

  <section class="post post-boost">
    <p class="headline">A natural way to<br>boost GLP-1 - no<br>injections, no<br>side effects, just<br>real results.<span>Here's how it<br>works</span></p>
    <p class="handle">@RKMarlowLive</p>
  </section>

  <section class="post post--outlined post-lied">
    <h2 class="title">You've been lied to</h2>
    <p class="sub">- 'Just eat less and exercise<br>more' doesn't work<br>in menopause</p>
    <p class="handle">@RKMarlowLive</p>
  </section>

  <section class="post post-fault">
    <h2 class="title">That stubborn<br>belly fat isn't<br>your fault</h2>
    <p class="sub">- Here's what no one tells you.</p>
    <p class="handle">@RKMarlowLive</p>
  </section>

  <section class="post post-frustrated">
    <h2 class="title">Frustrated with belly<br>fat that won't budge?</h2>
    <p class="body">I've got the solution that finally worked for me-no crazy diets required.</p>
    <p class="handle">@RKMarlowLive</p>
  </section>

  <section class="post post-hormones">
    <h2 class="title">Sis, your<br>hormones<br>are out of whack</h2>
    <p class="sub">- that's why the weight<br>won't budge!</p>
    <p class="handle">@RKMarlowLive</p>
  </section>

  <section class="post post-finally">
    <h2 class="word">Finally</h2>
    <p class="sub">-A natural solution<br>that flattens<br>your belly and eases<br>stomach bloat</p>
    <p class="handle">@RKMarlowLive</p>
  </section>

  <section class="post post-overnight">
    <svg class="strokes" width="271" height="271" viewBox="0 0 271 271" aria-hidden="true">
      <path d="M0 43 L105 10" stroke="#d4145a" stroke-width="2" fill="none" stroke-linecap="round"/>
      <path d="M151 254 L271 218" stroke="#d4145a" stroke-width="2" fill="none" stroke-linecap="round"/>
    </svg>
    <p class="message">One supplement,<br>one night;<br>your belly bloat<br>could be gone by<br>morning.<span>Here's how it<br>works!</span></p>
    <p class="handle">@RKMarlowLive</p>
  </section>

  <section class="post post-bloating">
    <h2 class="title">Struggling with<br>bloating and belly<br>fat?</h2>
    <p class="sub">Try this natural solution<br>tonight, and wake up<br>feeling lighter!</p>
    <p class="handle">@RKMarlowLive</p>
  </section>

  <section class="post post-wake">
    <h2 class="title">Wake up tomorrow<br>with a flatter belly–<br>yes, this overnight<br>remedy works like<br>magic!</h2>
    <p class="handle">@RKMarlowLive</p>
  </section>

</main>
</body>
</html>
```